Business Cards

We are an innovating group of real estate investors who buy beat up house's, fix them up, and resell them. We are in need of a business card that is catchy and stands out. We want it to say something like " Quick Key Home Buyers" Call us first

Industry/Entity Type

Business

Requirements
Must have
• Our logo which is updated

```html
<!DOCTYPE html>
<html lang="en">
<head>
<meta charset="utf-8">
<title>Quick Key Home Buyers – Business Card</title>
<link rel="stylesheet" href="https://fonts.googleapis.com/css2?family=Open+Sans:wght@400;700&display=swap">
<style>
  :root {
    --backdrop: #d6d6d6;
    --card: #3a3a3a;
    --card-band: #333333;
    --lime: #8dc63f;
    --lime-dark: #79ad32;
    --stripe-light: #f2f2f2;
    --stripe-mid: #bdbdbd;
    --text-light: #ffffff;
    --text-soft: #cfcfcf;
  }
  * { box-sizing: border-box; margin: 0; padding: 0; }
  html, body { width: 1200px; height: 900px; overflow: hidden; }
  body {
    background: var(--backdrop);
    font-family: "Open Sans", Arial, sans-serif;
    display: flex;
    flex-direction: column;
    align-items: center;
    justify-content: center;
    gap: 40px;
  }
  .card {
    position: relative;
    width: 700px;
    height: 400px;
    background: var(--card);
    overflow: hidden;
    box-shadow: 0 6px 18px rgba(0,0,0,0.25);
  }
  .brand {
    display: flex;
    align-items: center;
    gap: 14px;
  }
  .brand-square {
    width: 46px;
    height: 46px;
    background: var(--lime);
    flex: none;
  }
  .brand-name {
    font-weight: 700;
    font-size: 30px;
    line-height: 1.2;
    color: var(--lime);
    letter-spacing: -0.3px;
    white-space: nowrap;
  }
  .tagline {
    font-size: 12px;
    line-height: 1.4;
    color: var(--text-soft);
  }
  .card-front .brand-block {
    position: absolute;
    left: 0; right: 0;
    top: 100px;
    display: flex;
    flex-direction: column;
    align-items: center;
  }
  .card-front .brand-inner { display: flex; flex-direction: column; }
  .card-front .tagline { margin-left: 64px; margin-top: 2px; }
  .contact-band {
    position: absolute;
    left: 0; right: 0;
    top: 240px;
    height: 82px;
    background: var(--card-band);
    display: grid;
    grid-template-columns: 1fr 1fr 1fr;
    align-items: center;
    padding: 0 40px;
  }
  .contact-group { display: flex; flex-direction: column; gap: 10px; }
  .contact-item {
    display: flex;
    align-items: center;
    gap: 10px;
    font-size: 12px;
    color: var(--text-light);
  }
  .contact-item svg { width: 13px; height: 13px; flex: none; }
  .contact-group.web { justify-self: end; }
  .accent-stripe {
    position: absolute;
    left: 0; right: 0;
    top: 330px;
    height: 16px;
    background: linear-gradient(var(--stripe-light), var(--stripe-mid));
  }
  .accent-band {
    position: absolute;
    left: 0; right: 0; bottom: 0;
    height: 54px;
    background: linear-gradient(var(--lime), var(--lime-dark));
  }
  .card-back .brand-stack {
    position: absolute;
    left: 0; right: 0;
    top: 60px;
    display: flex;
    flex-direction: column;
    align-items: center;
  }
  .card-back .brand-square { width: 64px; height: 64px; margin-bottom: 22px; }
  .card-back .brand-name { color: var(--text-light); }
  .card-back .tagline { margin-top: 2px; }
</style>
</head>
<body>

  <section class="card card-front">
    <div class="brand-block">
      <div class="brand-inner">
        <div class="brand">
          <span class="brand-square"></span>
          <span class="brand-name">QUICK KEY HOME BUYERS</span>
        </div>
        <p class="tagline">Call us first</p>
      </div>
    </div>

    <div class="contact-band">
      <div class="contact-group">
        <span class="contact-item">
          <svg viewBox="0 0 12 12"><path d="M6 0.5a3.8 3.8 0 0 0-3.8 3.8C2.2 7.2 6 11.5 6 11.5s3.8-4.3 3.8-7.2A3.8 3.8 0 0 0 6 0.5zm0 5.3a1.5 1.5 0 1 1 0-3 1.5 1.5 0 0 1 0 3z" fill="var(--lime)"/></svg>
          Address
        </span>
      </div>
      <div class="contact-group">
        <span class="contact-item">
          <svg viewBox="0 0 12 12"><path d="M2.5 0.8l2 2.2-1 1.3c0.6 1.5 1.7 2.6 3.2 3.2l1.3-1 2.2 2-1 2.2C5 10.5 1.5 7 0.8 2.3z" fill="var(--lime)"/></svg>
          Telephone
        </span>
        <span class="contact-item">
          <svg viewBox="0 0 12 12"><rect x="3" y="1" width="6" height="3" fill="var(--lime)"/><rect x="1" y="4.5" width="10" height="5" rx="1" fill="var(--lime)"/><rect x="3" y="8" width="6" height="3" fill="var(--card-band)" stroke="var(--lime)" stroke-width="1"/></svg>
          Fax
        </span>
      </div>
      <div class="contact-group web">
        <span class="contact-item">
          <svg viewBox="0 0 12 12"><circle cx="6" cy="6" r="5" fill="none" stroke="var(--lime)" stroke-width="1.3"/><ellipse cx="6" cy="6" rx="2" ry="5" fill="none" stroke="var(--lime)" stroke-width="1"/><line x1="1" y1="6" x2="11" y2="6" stroke="var(--lime)" stroke-width="1"/></svg>
          www.yourwebsite.com
        </span>
        <span class="contact-item">
          <svg viewBox="0 0 12 12"><rect x="0.8" y="2.5" width="10.4" height="7" fill="var(--lime)"/><path d="M0.8 2.5L6 6.5l5.2-4" fill="none" stroke="var(--card-band)" stroke-width="1"/></svg>
          your@email.com
        </span>
      </div>
    </div>

    <div class="accent-stripe"></div>
    <div class="accent-band"></div>
  </section>

  <section class="card card-back">
    <div class="brand-stack">
      <span class="brand-square"></span>
      <span class="brand-name">QUICK KEY HOME BUYERS</span>
      <p class="tagline">Call us first</p>
    </div>
    <div class="accent-stripe"></div>
    <div class="accent-band"></div>
  </section>

</body>
</html>
```